Tri Fold Flyer for an IT Consulting Company

We need to redesign a retail flyer and gear it towards our Commercial/Small Business/Corporate clients. We are moving away from all retail services and are committed to the Business customer, specifically small business. Our goal is to have a Color Tri Fold that can be printed or emailed to a prospective customer. We want to have key points that grab the readers attention and peak their interest to call for more information. In addition we want to focus on our Strengths:

We specialize in Small Business Information Technology Services like:
Support Services for Servers, workstations, Networks, Firewalls, Virtual Machines,

Cloud Based Services - Centralized file storage, Email hosting, Website hosting, Software on Demand Services.

On site and Remote support Services - Computer hardware and software, virus Removal, Security, New computer Sales and Service

VPN Services (Securely connect remote offices)

Firewall Sales and Service - Stop Hackers, Secure Data, Monitor/Restrict Employee Internet Access.

Virtualization Services: Convert Physical Servers into Virtual Services, scale easier and reduce resources (manpower and money)

Virus Removal - Stop data theft, reduce email SPAM, secure data.

Offsite Data Backup - Secure nightly automated offsite data backup to the cloud.
Updates

We want to take this flyer and do a few things

 

1)      Makeit more professional and less appeal to the retail crowd. (remove the whitemen, etc..) We are targeting small business customers (less than 50 computers)and NO retail.

2)      Wewant to make this into a Trifold that we can pass out to our prospective clientswhen we do a cold call.  The outside needs to be catchy on the fold thatyou see so we “sell them a message”  and get logo awareness and brandingin their head. I was thinking something catchy like:

·Small Business Computer Repair

Or

·Fixed Cost IT Support Services

Keep the Design ideas flowing, they are starting to look good!

Target Market(s)

Our Target market is the small business client that has less than 50 employees/computers and needs an IT consulting firm to help them with either outsourcing or support services. We offer remote support, and on-site support and our claim to fame is dedicated support staff committed to personal service.

Industry/Entity Type

Computer

Requirements
Must have
• Must be a clean, professional, Tri fold that can be handed to a client looking for our services. It can be setup as a mailer but that is not the intent of the Tri-Fold. It Must help sell our services and entice the customer to give us a call.
Nice to have
• Color, Key focal points, modern Artistic Style, Marketing genius and the ability to set us apart from the competition.
Should not have
• Should not look cheap, cheesy, fun or silly. We are after a more serious crowd that is looking for professional support and positive attitude that we can provide.

```html
<!DOCTYPE html>
<html lang="en">
<head>
<meta charset="utf-8">
<title>Harborline Computer Services – Tri-Fold</title>
<link rel="stylesheet" href="https://fonts.googleapis.com/css2?family=PT+Sans:ital,wght@0,400;0,700;1,700&family=Open+Sans:ital,wght@1,800&display=swap">
<style>
:root{
  --navy:#1b3a7c;
  --navy-dark:#122b60;
  --ink:#4a4a4a;
  --panel-light:#f4f5f7;
  --panel-mid:#e3e6eb;
  --gold:#d8a928;
  --white:#ffffff;
}
*{box-sizing:border-box;margin:0;padding:0}
html,body{width:805px;height:1200px;overflow:hidden;background:var(--white)}
body{position:relative;font-family:"PT Sans",Arial,sans-serif;color:var(--ink)}
.sheet{position:absolute;left:37px;width:731px;height:520px;overflow:hidden;
  background:linear-gradient(170deg,var(--panel-light) 0%,var(--white) 45%,var(--panel-mid) 100%)}
.sheet--outside{top:42px}
.sheet--inside{top:622px}
.panel{position:absolute;top:0;height:520px}
.panel--left{left:0;width:248px}
.panel--mid{left:248px;width:243px}
.panel--right{left:491px;width:240px}
.panel--navy{background:var(--navy)}
.bar{background:var(--navy);color:var(--white);font-weight:700;display:flex;align-items:center}
.bar--head{height:38px;padding-left:15px;font-size:16px}
.bar--section{height:26px;justify-content:center;font-size:14px;border:2px solid var(--white);outline:1px solid var(--navy)}
.copy{position:absolute;left:15px;right:10px;font-size:12px;line-height:14.3px;text-align:justify}
.copy p+p{margin-top:12px}
.copy--light{color:var(--white)}
.badges{position:absolute;display:flex;gap:10px;align-items:center}
.badge-rect{width:52px;height:14px;background:#2b2b2b;border-radius:2px}
.badge-rect--long{width:100px;height:22px;background:var(--white);border:1px solid #333}
.badge-circle{width:36px;height:36px;border-radius:50%;background:#b3261e;border:3px solid #e5c9c6}
.badge-circle--grey{background:#e9e9ec;border-color:#b9bcc3}
.os-dot{width:28px;height:28px;border-radius:50%;background:#9aa0aa}
.division{position:absolute;left:15px;top:411px;font-size:12px}
.division-name{position:absolute;left:90px;top:434px;font-size:12px;color:#111;letter-spacing:.5px}
.footnote{position:absolute;right:12px;top:458px;font-size:7px;color:#111}
.mid-title{position:absolute;left:10px;top:12px;font-size:16px;font-weight:700;color:var(--white)}
.contact{position:absolute;left:0;width:243px;text-align:center;color:var(--white);font-size:16px;line-height:17px}
.brand{position:absolute;display:flex;align-items:center;gap:8px}
.brand-mark{width:20px;height:20px;border-radius:50%;background:var(--navy);flex:none}
.brand-name{font-size:15px;font-weight:700;color:var(--navy);letter-spacing:2.5px;line-height:16px;text-transform:uppercase}
.photo{position:absolute}
.tagline{position:absolute;left:8px;top:386px;font-family:"Open Sans",Verdana,sans-serif;font-style:italic;font-weight:800;font-size:20px;line-height:24px;color:var(--navy)}
.wave{position:absolute;left:0;bottom:0;width:731px;height:70px}
.web{position:absolute;left:0;width:731px;text-align:center;color:var(--white);font-size:11.5px;letter-spacing:1px;top:495px}
.web--spaced{letter-spacing:8px;font-size:14px;top:486px;padding-left:160px}
.list{list-style:none;font-size:12px;line-height:14.3px;position:absolute}
.list li{position:relative;padding-left:10px}
.list li::before{content:"";position:absolute;left:0;top:5px;width:5px;height:5px;border-radius:50%;background:var(--navy)}
.sheet-head-mid{position:absolute;left:0;top:0;width:243px;height:72px;background:var(--navy);color:var(--white);font-weight:700;font-size:14px;line-height:16px;text-align:center;padding-top:18px}
.section{position:absolute;left:0;right:0}
.call{position:absolute;left:0;width:240px;text-align:center;top:444px;font-size:17px;color:var(--navy)}
</style>
</head>
<body>

<!-- Outside of the tri-fold -->
<section class="sheet sheet--outside">
  <div class="panel panel--left">
    <div class="bar bar--head">Experience the HCS Difference</div>
    <div class="copy" style="top:50px">
      <p>Allow us to come to your home or office for a free con-sultation.</p>
      <p>We will evaluate your present system and computers, and offer free advice that will as-sist you in your decisions going forward. Whether it be new computer purchases, up-grades, support, data backup, security, wireless services, internet access or any of our other products and services, HCS will be with you every step of the way.</p>
    </div>
    <div class="badges" style="left:20px;top:224px"><span class="badge-rect"></span><span class="badge-rect badge-rect--long"></span></div>
    <div class="badges" style="left:80px;top:258px"><span class="badge-circle"></span><span class="badge-circle badge-circle--grey"></span></div>
    <div class="copy" style="top:307px"><p>We can handle any prob-lem on a number of platforms including desk-top, server, mobile systems and many others</p></div>
    <div class="badges" style="left:22px;top:362px;gap:22px"><span class="os-dot"></span><span class="os-dot"></span><span class="os-dot"></span><span class="os-dot" style="width:72px;border-radius:14px"></span></div>
    <div class="division">A Retail Division of:</div>
    <div class="division-name">Ardent Technologies</div>
    <div class="footnote">* Ask for details.</div>
  </div>

  <div class="panel panel--mid panel--navy">
    <div class="mid-title">Why Choose Us?</div>
    <div class="copy copy--light" style="top:48px;left:10px;right:12px">
      <p>We are Harborline Computer Services, East-ern North Carolina’s leading Computer Sales and Service provider. With over 23 years of experience, have the knowledge and skills to get the job done right the first time.</p>
      <p>We provide a money back guarantee*. You have absolutely noth-ing to lose except the hours of your day wasted by trying to fix it by yourself.</p>
      <p>Call us today to set up a FREE consultation and get your computer and network run-ning smoothly again.</p>
    </div>
    <div class="contact" style="top:359px">Questions?<br>Call us at (555) 014-2290</div>
    <div class="contact" style="top:409px">214-C West Alder Ave<br>Kinston Falls, NC 27999</div>
  </div>

  <div class="panel panel--right">
    <div class="brand" style="left:22px;top:58px"><span class="brand-mark"></span><span class="brand-name">Harborline<br>Computer Services</span></div>
    <svg class="photo" style="left:0;top:110px" width="240" height="270" viewBox="0 0 240 270" role="img" aria-label="Photo of a technician working inside an open computer tower">
      <defs><radialGradient id="photoTone" cx=".5" cy=".45" r=".6"><stop offset="0" stop-color="#c9d7e6"/><stop offset="1" stop-color="#6d87a8"/></radialGradient></defs>
      <circle cx="175" cy="130" r="135" fill="var(--navy)"/>
      <circle cx="175" cy="130" r="127" fill="url(#photoTone)"/>
    </svg>
    <div class="tagline">Small<br>Business<br>ComputerRepair</div>
  </div>

  <svg class="wave" viewBox="0 0 731 70" preserveAspectRatio="none">
    <path d="M0,18 Q380,14 731,50 L731,70 L0,70Z" fill="#6f86b3"/>
    <path d="M0,24 Q380,20 731,56 L731,70 L0,70Z" fill="var(--navy)"/>
  </svg>
  <div class="web">www.HarborlineComputerServices.com</div>
</section>

<!-- Inside of the tri-fold -->
<section class="sheet sheet--inside">
  <div class="panel panel--left">
    <div class="bar bar--head">Here to Serve YOU</div>
    <div class="copy" style="top:50px">
      <p>Harborline Computer Services is proud to be serving Eastern North Carolina. Opened in 1994 we are based on “old-fashioned” values of honesty, integrity, and dedication to excellence. HCS has a 100% Satisfaction Guaranteed policy, and we will do what ever it takes to make sure the client is happy with our products, services and atti-tude. Having been in the industry since its infancy, we know the technology inside and out. You will not find a more qualified and skilled group of people to help you use, un-derstand, purchase and maintain comput-ers, networks and the associated equip-ment than HCS.</p>
    </div>
    <svg class="photo" style="left:18px;top:290px" width="160" height="210" viewBox="0 0 160 210" role="img" aria-label="Photo of black server rack cabinets">
      <defs><linearGradient id="rackTone" x1="0" x2="1"><stop offset="0" stop-color="#0d0f14"/><stop offset=".5" stop-color="#3a3f4a"/><stop offset="1" stop-color="#14171d"/></linearGradient></defs>
      <path d="M8,20 L120,0 L160,10 L160,200 L20,210 L8,200Z" fill="url(#rackTone)"/>
    </svg>
    <svg class="photo" style="left:160px;top:270px" width="76" height="76" viewBox="0 0 76 76" role="img" aria-label="Satisfaction guarantee seal">
      <circle cx="38" cy="38" r="36" fill="var(--gold)"/>
      <rect x="4" y="32" width="68" height="14" fill="#2b2b2b"/>
    </svg>
  </div>

  <div class="panel panel--mid">
    <div class="sheet-head-mid">We specialize in Small Business<br>Information Technology Services<br>like:</div>
    <ul class="list" style="left:44px;top:94px">
      <li>Support Services for Servers,</li><li>workstations,</li><li>Networks,</li><li>Firewalls,</li><li>Virtual Machines,</li>
    </ul>
    <div class="section bar bar--section" style="top:172px">Cloud Based Services</div>
    <ul class="list" style="left:44px;top:205px">
      <li>Centralized file storage,</li><li>Email hosting,</li><li>Website hosting,</li><li>Software on Demand Services.</li>
    </ul>
    <div class="section bar bar--section" style="top:270px">On site and Remote support Services</div>
    <ul class="list" style="left:28px;top:304px">
      <li>Computer hardware and software,</li><li>virus Removal,</li><li>Security,</li><li>New computer Sales and Service</li>
    </ul>
    <div class="section bar bar--section" style="top:376px">VPN Services</div>
    <ul class="list" style="left:28px;top:411px"><li>Securely connect remote offices)</li></ul>
  </div>

  <div class="panel panel--right">
    <div class="bar bar--head" style="justify-content:center;padding-left:0;font-size:14.5px">Firewall Sales and Service</div>
    <ul class="list" style="left:16px;top:46px;right:8px">
      <li>Stop Hackers,</li><li>Secure Data,</li><li>Monitor/Restrict Employee Internet Access.</li>
    </ul>
    <div class="section bar bar--section" style="top:112px">Virtualization Services</div>
    <ul class="list" style="left:16px;top:145px;right:8px">
      <li>Convert Physical Servers into Virtual Services,</li><li>scale easier and reduce resources (manpower and money)</li>
    </ul>
    <div class="section bar bar--section" style="top:208px">Virus Removal</div>
    <ul class="list" style="left:56px;top:242px">
      <li>Stop data theft,</li><li>reduce email SPAM,</li><li>secure data.</li>
    </ul>
    <div class="section bar bar--section" style="top:300px">Offsite Data Backup</div>
    <ul class="list" style="left:12px;top:335px;right:8px"><li>Secure nightly automated offsite data backup to the cloud.</li></ul>
    <div class="brand" style="left:38px;top:390px"><span class="brand-mark"></span><span class="brand-name" style="font-size:13px">Harborline<br>Computer Services</span></div>
    <div class="call">Call us at (555) 014-2290</div>
  </div>

  <svg class="wave" viewBox="0 0 731 70" preserveAspectRatio="none">
    <path d="M0,4 Q380,4 731,34 L731,70 L0,70Z" fill="#6f86b3"/>
    <path d="M0,10 Q380,10 731,40 L731,70 L0,70Z" fill="var(--navy)"/>
  </svg>
  <div class="web web--spaced">www.HarborlineComputerServices.com</div>
</section>

</body>
</html>
```